body balm label design

body balm tube design, current label design for other similar products
Need to have a design which can interchange between 3 different solutions
Quiet Orchard (Lavender + Vanilla)
Copper Trail (Eucalyptus + Mint)
Fern Hollow (Bergamot + Cedarwood)
Tube size:
2.5h x 3.25 w
Target Market(s)
natural, solution focused
Requirements
Must have
- relatable to existing brand designs, focus on features and benefits

```html
<!DOCTYPE html>
<html lang="en">
<head>
<meta charset="utf-8">
<title>Willow Bloom Body Balm Labels</title>
<link rel="stylesheet" href="https://fonts.googleapis.com/css2?family=Cormorant+Garamond:wght@400;500&family=Pinyon+Script&family=Source+Code+Pro:wght@400;700&display=swap">
<style>
  :root {
    --canvas: #dcdcdc;
    --paper: #ffffff;
    --ink: #6c8190;
    --orchard: #a57bb8;
    --trail: #71866a;
    --hollow: #d8803a;
  }
  * { box-sizing: border-box; margin: 0; padding: 0; }
  html, body { width: 1200px; height: 849px; overflow: hidden; background: var(--canvas); }
  .sheet {
    width: 1200px; height: 849px;
    display: flex; align-items: center; justify-content: center; gap: 50px;
  }
  .pair { display: flex; gap: 18px; }
  .label {
    position: relative; width: 165px; height: 456px;
    background: linear-gradient(var(--paper) 0 187px, var(--band) 187px);
    color: var(--ink); font-family: "Source Code Pro", monospace;
  }
  .quiet-orchard { --band: var(--orchard); }
  .copper-trail { --band: var(--trail); }
  .fern-hollow { --band: var(--hollow); }

  .brand {
    position: absolute; left: 0; right: 0;
    text-align: center; font-family: "Cormorant Garamond", serif;
    font-weight: 400; font-size: 15px; letter-spacing: .5px; color: var(--ink);
  }
  .product-type {
    position: absolute; left: 0; right: 0; text-align: center;
    font-family: "Pinyon Script", cursive; font-size: 24px; color: var(--ink);
  }
  .scent-frame {
    position: absolute; left: 8px; right: 8px;
    background: var(--paper); border: 1px solid var(--band);
    outline: 2px solid var(--paper);
  }
  .scent-frame::after {
    content: ""; position: absolute; inset: 2px; border: 1px solid var(--band); opacity: .35;
  }
  .scent-name {
    display: block; text-align: center; padding-top: 9px;
    font-family: "Cormorant Garamond", serif; font-weight: 500;
    font-size: 20px; letter-spacing: 4px; line-height: 1;
  }
  .scent-accent {
    display: flex; align-items: center; justify-content: flex-end; gap: 4px;
    padding-right: 16px; margin-top: -2px;
    font-family: "Pinyon Script", cursive; font-size: 17px; line-height: 1;
  }
  .scent-accent::before { content: ""; width: 38px; height: 1px; background: var(--ink); opacity: .6; }
  .botanical {
    display: block; margin: 6px auto 0; width: 118px; height: 92px;
    background: radial-gradient(ellipse at center, rgba(108,129,144,.18), rgba(108,129,144,.04) 70%);
  }
  .front .brand { top: 48px; }
  .front .product-type { top: 66px; }
  .front .scent-frame { top: 115px; height: 154px; }

  .benefit-row {
    position: absolute; top: 298px; left: 10px; right: 10px;
    display: flex; justify-content: space-between;
  }
  .benefit { width: 44px; text-align: center; font-size: 5.5px; line-height: 1.3; color: #fff; letter-spacing: .3px; }
  .benefit svg { display: block; margin: 0 auto 4px; }
  .net-weight {
    position: absolute; left: 0; right: 0; text-align: center;
    font-size: 10.5px; color: #fff; letter-spacing: .4px;
  }
  .front .net-weight { top: 402px; }

  .back .brand { top: 77px; }
  .back .product-type { top: 94px; }
  .back .scent-frame { top: 140px; height: 72px; }
  .claims { position: absolute; top: 227px; left: 0; right: 0; text-align: center; color: #fff; }
  .claims .icons { display: flex; justify-content: center; gap: 18px; }
  .claims p { font-size: 5.2px; letter-spacing: .3px; margin-top: 4px; }
  .ingredients {
    position: absolute; top: 268px; left: 10px; right: 10px;
    color: #fff; font-size: 5.3px; line-height: 8.7px; text-align: justify;
  }
  .ingredients h3 { text-align: center; font-size: 5.6px; font-weight: 700; letter-spacing: .3px; }
  .back .net-weight { top: 362px; }
  .maker {
    position: absolute; top: 384px; left: 0; right: 0; text-align: center;
    color: #fff; font-size: 5.6px; line-height: 10.5px; letter-spacing: .3px;
  }
  .maker strong { font-weight: 700; }
  .web {
    position: absolute; top: 428px; left: 0; right: 0; text-align: center;
    color: #fff; font-size: 5.6px; letter-spacing: .3px;
  }
</style>
</head>
<body>
<svg width="0" height="0" style="position:absolute">
  <defs>
    <symbol id="leaf" viewBox="0 0 40 40">
      <circle cx="20" cy="20" r="19" fill="#fff"/>
      <path d="M20 28 C12 24 11 15 13 11 C19 13 22 20 20 28Z M20 28 C28 24 29 15 27 11 C21 13 18 20 20 28Z" fill="var(--band)"/>
    </symbol>
    <symbol id="heart" viewBox="0 0 40 40">
      <circle cx="20" cy="20" r="19" fill="#fff"/>
      <path d="M20 29 L11 20 C7 16 10 10 15 11 C17 11.5 19 13 20 15 C21 13 23 11.5 25 11 C30 10 33 16 29 20Z" fill="var(--band)"/>
    </symbol>
    <symbol id="badge" viewBox="0 0 40 40">
      <rect x="9" y="3" width="22" height="34" rx="11" fill="#fff"/>
    </symbol>
    <symbol id="diamond" viewBox="0 0 40 40">
      <rect x="9" y="9" width="22" height="22" transform="rotate(45 20 20)" fill="#fff"/>
      <path d="M20 25 L15 20 C13 18 15 15 17.5 16 C18.5 16.4 19.5 17 20 18 C20.5 17 21.5 16.4 22.5 16 C25 15 27 18 25 20Z" fill="var(--band)"/>
    </symbol>
  </defs>
</svg>

<main class="sheet">
  <!-- Quiet Orchard -->
  <section class="pair quiet-orchard">
    <article class="label front">
      <h2 class="brand">WILLOW BLOOM</h2>
      <p class="product-type">Body Balm</p>
      <div class="scent-frame">
        <span class="scent-name">QUIET</span>
        <span class="scent-accent">Orchard</span>
        <span class="botanical" role="img" aria-label="Line drawing of lavender sprigs"></span>
      </div>
      <div class="benefit-row">
        <div class="benefit"><svg width="38" height="38"><use href="#leaf"/></svg>PLANT<br>BASED</div>
        <div class="benefit"><svg width="38" height="38"><use href="#heart"/></svg>VEGAN</div>
        <div class="benefit"><svg width="38" height="38"><use href="#badge"/></svg>CRUELTY<br>FREE</div>
      </div>
      <p class="net-weight">Net WT. 3oz / 8.5G</p>
    </article>
    <article class="label back">
      <h2 class="brand">WILLOW BLOOM</h2>
      <p class="product-type">Body Balm</p>
      <div class="scent-frame">
        <span class="scent-name">QUIET</span>
        <span class="scent-accent">Orchard</span>
      </div>
      <div class="claims">
        <div class="icons">
          <svg width="18" height="18"><use href="#leaf"/></svg>
          <svg width="18" height="18"><use href="#diamond"/></svg>
          <svg width="18" height="18"><use href="#badge"/></svg>
        </div>
        <p>PLANT BASED • VEGAN • CRUELTY FREE</p>
      </div>
      <div class="ingredients">
        <h3>INGREDIENTS:</h3>
        Organic Olive Fruit Oil (Olea Europaea), Organic Coconut Oil (Cocos Nucifera), Organic Shea Butter (Butyrospermum Parkii), Organic Jojoba Seed Oil (Simmondsia Chinensis), Rosehip Seed Oil (Rosa Canina), Vitamin E (Tocopherol), Sunflower Seed Oil (Helianthus Annuus), Vanilla Aroma, Mentha Piperita (Peppermint) Leaf Oil, Dipteryx Odorata (Tonka Bean) Oil
      </div>
      <p class="net-weight">Net WT. 3oz / 8.5G</p>
      <p class="maker"><strong>MADE BY WILLOW BLOOM</strong><br>FAIRHAVEN. AB T0L 4K2<br>MADE IN CANADA 100% NATURAL</p>
      <p class="web">www.willowbloom.ca</p>
    </article>
  </section>

  <!-- Fern Hollow -->
  <section class="pair fern-hollow">
    <article class="label front">
      <h2 class="brand">WILLOW BLOOM</h2>
      <p class="product-type">Body Balm</p>
      <div class="scent-frame">
        <span class="scent-name">FERN</span>
        <span class="scent-accent">Hollow</span>
        <span class="botanical" role="img" aria-label="Line drawing of bergamot fruit and cedar sprig"></span>
      </div>
      <div class="benefit-row">
        <div class="benefit"><svg width="38" height="38"><use href="#leaf"/></svg>PLANT<br>BASED</div>
        <div class="benefit"><svg width="38" height="38"><use href="#heart"/></svg>VEGAN</div>
        <div class="benefit"><svg width="38" height="38"><use href="#badge"/></svg>CRUELTY<br>FREE</div>
      </div>
      <p class="net-weight">Net WT. 3oz / 8.5G</p>
    </article>
    <article class="label back">
      <h2 class="brand">WILLOW BLOOM</h2>
      <p class="product-type">Body Balm</p>
      <div class="scent-frame">
        <span class="scent-name">FERN</span>
        <span class="scent-accent">Hollow</span>
      </div>
      <div class="claims">
        <div class="icons">
          <svg width="18" height="18"><use href="#leaf"/></svg>
          <svg width="18" height="18"><use href="#diamond"/></svg>
          <svg width="18" height="18"><use href="#badge"/></svg>
        </div>
        <p>PLANT BASED • VEGAN • CRUELTY FREE</p>
      </div>
      <div class="ingredients">
        <h3>INGREDIENTS:</h3>
        Organic Olive Fruit Oil (Olea Europaea), Organic Coconut Oil (Cocos Nucifera), Organic Shea Butter (Butyrospermum Parkii), Organic Jojoba Seed Oil (Simmondsia Chinensis), Rosehip Seed Oil (Rosa Canina), Vitamin E (Tocopherol), Sunflower Seed Oil (Helianthus Annuus), Vanilla Aroma, Mentha Piperita (Peppermint) Leaf Oil, Dipteryx Odorata (Tonka Bean) Oil
      </div>
      <p class="net-weight">Net WT. 3oz / 8.5G</p>
      <p class="maker"><strong>MADE BY WILLOW BLOOM</strong><br>FAIRHAVEN. AB T0L 4K2<br>MADE IN CANADA 100% NATURAL</p>
      <p class="web">www.willowbloom.ca</p>
    </article>
  </section>

  <!-- Copper Trail -->
  <section class="pair copper-trail">
    <article class="label front">
      <h2 class="brand">WILLOW BLOOM</h2>
      <p class="product-type">Body Balm</p>
      <div class="scent-frame">
        <span class="scent-name">COPPER</span>
        <span class="scent-accent">Trail</span>
        <span class="botanical" role="img" aria-label="Line drawing of eucalyptus branch and mint"></span>
      </div>
      <div class="benefit-row">
        <div class="benefit"><svg width="38" height="38"><use href="#leaf"/></svg>PLANT<br>BASED</div>
        <div class="benefit"><svg width="38" height="38"><use href="#heart"/></svg>VEGAN</div>
        <div class="benefit"><svg width="38" height="38"><use href="#badge"/></svg>CRUELTY<br>FREE</div>
      </div>
      <p class="net-weight">Net WT. 3oz / 8.5G</p>
    </article>
    <article class="label back">
      <h2 class="brand">WILLOW BLOOM</h2>
      <p class="product-type">Body Balm</p>
      <div class="scent-frame">
        <span class="scent-name">COPPER</span>
        <span class="scent-accent">Trail</span>
      </div>
      <div class="claims">
        <div class="icons">
          <svg width="18" height="18"><use href="#leaf"/></svg>
          <svg width="18" height="18"><use href="#diamond"/></svg>
          <svg width="18" height="18"><use href="#badge"/></svg>
        </div>
        <p>PLANT BASED • VEGAN • CRUELTY FREE</p>
      </div>
      <div class="ingredients">
        <h3>INGREDIENTS:</h3>
        Organic Olive Fruit Oil (Olea Europaea), Organic Coconut Oil (Cocos Nucifera), Organic Shea Butter (Butyrospermum Parkii), Organic Jojoba Seed Oil (Simmondsia Chinensis), Rosehip Seed Oil (Rosa Canina), Vitamin E (Tocopherol), Sunflower Seed Oil (Helianthus Annuus), Vanilla Aroma, Mentha Piperita (Peppermint) Leaf Oil, Dipteryx Odorata (Tonka Bean) Oil
      </div>
      <p class="net-weight">Net WT. 3oz / 8.5G</p>
      <p class="maker"><strong>MADE BY WILLOW BLOOM</strong><br>FAIRHAVEN. AB T0L 4K2<br>MADE IN CANADA 100% NATURAL</p>
      <p class="web">www.willowbloom.ca</p>
    </article>
  </section>
</main>
</body>
</html>
```